Minimalist, Flat(Matte) design for a Beef Jerky packaging company. No bullshit company looking for a

Need a packaging design for a new Beef Jerky product(in English). The name of the company is 'Velmor' and thus the packaging should reflect the bullish, tough, and simple nature of the beef jerky product. The finished product should communicate simplicity, minimalism, yet toughness and strength.

The logo should be simple, with a minimal number of colors , and should be either all white/cream, or have some red as well. Main colors should be white, cream, tinted red, and matte black. I think 4 colors max would be best. The closest example to an existing package style would be Korvanti Dusk clove cigarettes( image attached).

It will be on a matte black standing pouch package. See image for package type. Package dimensions:

Dimension: Width x Gusset x Height
INCH : 5.125" (W) x 3.125" (G) x 8.125" (H)
MILLIMETER : 130mm (W) x 80mm (G) x 205mm (H)

I don't have anything totally specific so artistic liberty is encouraged, provided the colors are kept to a minimum and looks consistent with the simple nature of the brand and the matte black packaging.

Also attached an existing beef jerky package with a similar style to what we're looking for.

Industry/Entity Type

It Company

Colors
f59195
ffffff

Requirements
Must have
• Low contrast, flat and minimalist design.
Should not have
• A complicated design with many colors. Gawdy/flashy design. Bright colors. High contrast.

```html
<!DOCTYPE html>
<html lang="en">
<head>
<meta charset="utf-8">
<title>Velmor Beef Jerky – Peppered Pouch</title>
<link href="https://fonts.googleapis.com/css2?family=Oswald:wght@500;600&family=Cinzel:wght@700&display=swap" rel="stylesheet">
<style>
  :root{
    --backdrop:#d2d2d2;
    --pouch-black:#121212;
    --seal-black:#0c0c0c;
    --cream:#ede2cf;
    --tinted-red:#d8231c;
    --rule:#8f887e;
  }
  html,body{margin:0;padding:0;width:1200px;height:900px;overflow:hidden;background:var(--backdrop);}
  .canvas{position:relative;width:1200px;height:900px;}
  .pouch{
    position:absolute;left:412px;top:118px;width:443px;height:702px;
    background:var(--pouch-black);border-radius:4px 4px 2px 2px;
  }
  .pouch__seal{position:absolute;left:0;right:0;top:0;height:72px;background:var(--seal-black);border-bottom:1px solid #1e1e1e;}
  .brand{
    position:absolute;left:0;right:0;top:210px;
    display:flex;align-items:center;justify-content:center;gap:14px;
  }
  .brand__square{width:22px;height:22px;background:var(--tinted-red);}
  .brand__name{
    font-family:'Oswald',sans-serif;font-weight:600;font-size:62px;
    letter-spacing:3px;color:var(--cream);line-height:1;
  }
  .product{position:absolute;left:0;right:0;top:400px;text-align:center;color:var(--cream);}
  .product__kicker{
    font-family:'Oswald',sans-serif;font-weight:500;font-size:14px;
    letter-spacing:7px;line-height:1;margin:0;
  }
  .product__name{
    font-family:'Oswald',sans-serif;font-weight:600;font-size:62px;
    letter-spacing:2px;line-height:1;margin:12px 0 10px;
  }
  .product__rule{width:290px;height:1px;background:var(--rule);margin:0 auto;}
  .product__flavour{
    font-family:'Cinzel',serif;font-weight:700;font-size:46px;
    letter-spacing:1px;line-height:1;margin:14px 0 12px;
  }
  .product__kicker--below{margin-bottom:24px;}
  .product__weight{
    font-family:'Cinzel',serif;font-weight:700;font-size:12px;
    letter-spacing:0.5px;margin-top:34px;
  }
</style>
</head>
<body>
<div class="canvas">
  <div class="pouch">
    <div class="pouch__seal"></div>
    <div class="brand">
      <span class="brand__square"></span>
      <span class="brand__name">VELMOR</span>
    </div>
    <div class="product">
      <p class="product__kicker">HAND CRAFTED</p>
      <p class="product__name">BEEF JERKY</p>
      <p class="product__kicker product__kicker--below">SMALL BATCH</p>
      <div class="product__rule"></div>
      <p class="product__flavour">PEPPERED</p>
      <div class="product__rule"></div>
      <p class="product__weight">NET WT. 3 OZ</p>
    </div>
  </div>
</div>
</body>
</html>
```